Criação de Papelaria Profissional para Contabilidade & Finanças
" ESTOU INICANDO AGORA O ESCRITORIO DE CONTABILIDADE, QUERO ATUAR NO RAMO DE TREINAMENTO ATRAVÉS DO COACHING , FAZER CONSULTORIAS NA AREA CONTABIL, SERVIÇOS CONTABEIS EM GERAL, DESDE O MICROEMPREENDEDOR ATÉ O A EMPRESA DE GRANDE PORTE LUCRO REAL "

```html
<!DOCTYPE html>
<html lang="pt-BR">
<head>
<meta charset="UTF-8">
<title>Vantra – Papel Timbrado</title>
<link rel="stylesheet" href="https://fonts.googleapis.com/css2?family=Montserrat:wght@400;600;700;800&display=swap">
<style>
  :root {
    --backdrop: #e4e5e7;
    --paper: #ffffff;
    --navy: #101a3c;
    --gold: #c99a2e;
    --gold-light: #e8c56a;
    --ink: #3a3f4c;
    --muted: #8a8f99;
    --swoosh: #e9eaec;
  }
  * { box-sizing: border-box; margin: 0; padding: 0; }
  html, body { width: 1200px; height: 1200px; overflow: hidden; }
  body {
    background: var(--backdrop);
    font-family: "Montserrat", sans-serif;
    display: flex;
    align-items: center;
    justify-content: center;
  }
  .letterhead {
    position: relative;
    width: 778px;
    height: 1100px;
    background: var(--paper);
    box-shadow: 0 6px 24px rgba(0,0,0,0.12);
    overflow: hidden;
  }
  .brand {
    position: absolute;
    left: 64px;
    top: 58px;
    display: flex;
    align-items: center;
    gap: 12px;
  }
  .brand-mark {
    width: 30px;
    height: 30px;
    background: var(--navy);
  }
  .brand-text { display: flex; flex-direction: column; }
  .brand-name {
    font-weight: 800;
    font-size: 40px;
    letter-spacing: 1px;
    color: var(--navy);
    line-height: 1;
  }
  .brand-tagline {
    font-size: 9px;
    font-weight: 600;
    letter-spacing: 0.6px;
    color: var(--ink);
    text-transform: uppercase;
    margin-top: 4px;
  }
  .header-rule {
    position: absolute;
    left: 230px;
    top: 92px;
    width: 520px;
    height: 22px;
  }
  .background-swoosh {
    position: absolute;
    left: 0;
    top: 420px;
    width: 100%;
    height: 470px;
    background: linear-gradient(160deg, rgba(233,234,236,0) 0%, var(--swoosh) 45%, rgba(233,234,236,0.4) 100%);
  }
  .contacts {
    position: absolute;
    left: 64px;
    right: 64px;
    top: 1000px;
    display: flex;
    justify-content: space-between;
  }
  .contact-item { display: flex; gap: 7px; align-items: flex-start; }
  .contact-icon {
    width: 16px; height: 16px; flex: none;
    border-radius: 50%;
    background: var(--navy);
    display: flex; align-items: center; justify-content: center;
  }
  .contact-text {
    font-size: 9px;
    line-height: 1.45;
    color: var(--muted);
  }
  .footer-rule {
    position: absolute;
    right: 40px;
    top: 1046px;
    width: 150px;
    height: 2px;
    background: linear-gradient(90deg, rgba(201,154,46,0), var(--gold));
  }
  .footer-band {
    position: absolute;
    left: 0; right: 0; bottom: 0;
    height: 34px;
  }
</style>
</head>
<body>
  <main class="letterhead">
    <div class="brand">
      <span class="brand-mark"></span>
      <div class="brand-text">
        <span class="brand-name">VANTRA</span>
        <span class="brand-tagline">Consultoria Contábil &amp; Fiscal</span>
      </div>
    </div>

    <svg class="header-rule" viewBox="0 0 520 22" preserveAspectRatio="none">
      <defs>
        <linearGradient id="gold-rule" x1="0" x2="1">
          <stop offset="0" stop-color="#c99a2e" stop-opacity="0"/>
          <stop offset="0.2" stop-color="#c99a2e"/>
          <stop offset="0.85" stop-color="#e8c56a"/>
          <stop offset="1" stop-color="#c99a2e" stop-opacity="0"/>
        </linearGradient>
      </defs>
      <path d="M0 20 Q40 18 120 18 L430 18 Q470 18 520 2" fill="none" stroke="url(#gold-rule)" stroke-width="2"/>
    </svg>

    <div class="background-swoosh" role="img" aria-label="Faint grey abstract swoosh decoration"></div>

    <div class="contacts">
      <div class="contact-item">
        <span class="contact-icon">
          <svg width="9" height="9" viewBox="0 0 24 24"><path fill="#fff" d="M6.6 10.8a15 15 0 0 0 6.6 6.6l2.2-2.2c.3-.3.7-.4 1-.2 1.1.4 2.3.6 3.6.6.6 0 1 .4 1 1V20c0 .6-.4 1-1 1A17 17 0 0 1 3 4c0-.6.4-1 1-1h3.5c.6 0 1 .4 1 1 0 1.3.2 2.5.6 3.6.1.3 0 .7-.2 1z"/></svg>
        </span>
        <p class="contact-text">(41) 3000-1200<br>(41) 99000-1200</p>
      </div>
      <div class="contact-item">
        <span class="contact-icon">
          <svg width="9" height="9" viewBox="0 0 24 24"><path fill="#fff" d="M12 2a7 7 0 0 0-7 7c0 5.2 7 13 7 13s7-7.8 7-13a7 7 0 0 0-7-7zm0 9.5A2.5 2.5 0 1 1 12 6.5a2.5 2.5 0 0 1 0 5z"/></svg>
        </span>
        <p class="contact-text">Rua das Acácias, 120 sl 04<br>Centro · Curitiba/PR · CEP 80000-000</p>
      </div>
      <div class="contact-item">
        <span class="contact-icon">
          <svg width="9" height="9" viewBox="0 0 24 24"><path fill="#fff" d="M3 5h18v14H3zm2 2v.5l7 4.5 7-4.5V7l-7 4.5z"/></svg>
        </span>
        <p class="contact-text">contato@vantracontabil.com.br<br>www.vantracontabil.com.br</p>
      </div>
    </div>

    <div class="footer-rule"></div>

    <svg class="footer-band" viewBox="0 0 778 34" preserveAspectRatio="none">
      <path d="M0 10 Q300 4 778 8 L778 34 L0 34 Z" fill="#c99a2e"/>
      <path d="M0 14 Q300 8 778 12 L778 34 L0 34 Z" fill="#101a3c"/>
    </svg>
  </main>
</body>
</html>
```